Systems and Technology Consultants - Website

Design & Build a website for a new company which operates in the Systems and Technology space for Transportation, Government and Commercial sectors.

Overall design should be minimalist in nature.
Should also have a feed that provides news and event updates on the main page.
Logo has already been awarded and should be incorporated into the site.

We like the overall layout, functionality and simplicity of the below sites. Submitted designs could be similar to or a combination of the aspects on these sites, or perhaps a whole different concept - we are open to new ideas.
Vortrane.com
Merp.it

Update 1 Dated 27 May 2014

All I am moving away from the Merp.it website and would like it to be more aligned with Vortrane.com not only in layout but in functionality. I will be extending the deadline of this design brief for two weeks to incorporate additional requirements and will add addtional funding to the project.

Apologies for not having more information available to provide but with so many submissions its getting confusing.

Thanks Dermot
Updates

Please note that the brief has been updated and the deadline has been extended.

Important: We will need two language versions of the website, English and Arabic; the website is hosted on HostPeak

Hello All, Thank you for your submissions. We have narrowed it down to the final 6 designers and I just wanted to take a moment and provide a bit of feedback regarding the concepts that we like and the modifications we are looking for. First, let me mention some of the design functions we like. - At the top of the homepage we really like the "region" or "language" tab so that the website can be viewed in both English and Arabic. - We like the homepage to have clear color variation so that the different sections of the homepage are distinct. Additionally, we like the bottom portion of the homepage to be in red. We feel that draws attention to our contact information. Again, we would like the colors to integrate black, gray-scale, red, etc. - Having a search tab at the top of the home page, or integrated into the main image, so that the site is easy to navigate. - We especially like the main image to have the scrolling tabs at the bottom so it is easy to browse the services offered (Consultancy, Solutions Architecture, Masters Systems Integration, Independent Design Review). - In regards to the services offered tab we really like the idea that a few people presented that have the outside of our logo with an icon in the middle of consultancy, solutions, etc., etc. Secondly, as mentioned in our brief we really enjoy the design of vortrane site. Specially, we enjoy the strong iconic images they use, the way the tabs at the top scroll easily, and contact us page that generates an email. Lastly, I've included some photos of the concept we have been working on. What we are trying to demonstrate is how our company offers a range of services that are essentially linked together. We provide individual services that when combined present the full service package. We would like this concept to be integrated into the over concept of our website. Please feel free to ask for clarification of any of the above points or contact us if you have any additional questions. We appreciate all of your hard work and are very excited to see the updated designs. Best, Miriam Dowbrook Plenvaro Senior Program Manager miriam.dowbrook@plenvaro-mail.com

Industry/Entity Type

Government

Font styles to use
Serif
Sans Serif

Requirements
Must have
• Must work on/adapt to various/mobile devices (responsive)
Must be simple and straightforward
Colors should be in line/matching with logo
2 language versions: English and Arabic (no Thai)
Services should be the first group/row of items after/below the main image
Note: the website will be hosted by hostpeak
Nice to have
• Submit feedback form
What's New section
The banner at the bottom of the site should not be too large; we would like a narrow one more
It would be nice if the header/top banner (with Home, About, etc. tabs) could stay in place as you scroll down (like Vortrane and Chatterly)
We will likely only use one image with a Company slogan on the Home page rather than a carousel of images to rotate through
Should not have
• This is the existing website: http://www.plenvaro-example.org
We do not like the animation, the way the banner icons/titles bounce
Not simple enough, we don't like the functionality or how pages load so slowly
We do not like the logo centered - it should be at the left
The banner and its tabs should not be towards the right, we would like them to be centered, to go all the way across and to be below the logo

```html
<!DOCTYPE html>
<html lang="en">
<head>
<meta charset="utf-8">
<title>Plenvaro International — Meet Your Goals</title>
<link rel="stylesheet" href="https://fonts.googleapis.com/css2?family=Oswald:wght@200;300;400;500;700&display=swap">
<style>
:root{
  --ink:#1d1d1d;
  --text:#2b2b2b;
  --muted:#6d6d6d;
  --paper:#ffffff;
  --paper-soft:#f7f7f7;
  --rule:#9a9a9a;
  --slate:#3d3d3d;
  --slate-deep:#343434;
  --green:#4c9168;
  --gold:#c99a16;
  --gold-deep:#a97e0c;
  --footer:#1f1f1f;
  --footer-tile:#3b3b3b;
  --footer-type:#f2f2f2;
  --copyright:#3e3e3e;
}
*{box-sizing:border-box;margin:0;padding:0}
html,body{width:693px;height:1200px;overflow:hidden}
body{position:relative;background:var(--paper);font-family:"Oswald",sans-serif;color:var(--text);text-transform:uppercase}

.site-header{position:absolute;left:0;top:0;width:693px;height:49px;background:var(--paper);border-bottom:1px solid #e4e4e4}
.brand{position:absolute;left:138px;top:15px;display:flex;align-items:center;gap:5px;font-weight:500;font-size:12px;letter-spacing:1.5px;color:var(--ink)}
.brand-mark{width:9px;height:9px;background:var(--ink)}
.main-nav{position:absolute;right:133px;top:22px;display:flex;align-items:center;gap:9px;font-size:7.5px;font-weight:500;color:var(--ink)}
.main-nav .is-current{color:var(--muted);text-decoration:underline}
.main-nav .sep{color:#999;font-size:7px}

.hero{position:absolute;left:0;top:50px;width:693px;height:326px}
.hero-photo{position:absolute;inset:0;background:
  radial-gradient(ellipse at 75% 60%,#1f1f1f 0%,rgba(31,31,31,0) 55%),
  linear-gradient(100deg,#c9c4bb 0%,#a7835f 28%,#7b5636 52%,#3a2d22 74%,#262321 100%)}
.hero-graphic{position:absolute;inset:0}
.contact-tab{position:absolute;left:0;top:69px;width:21px;height:80px;background:var(--paper);border-radius:0 5px 5px 0;display:flex;align-items:center;justify-content:center}
.contact-tab span{writing-mode:vertical-rl;transform:rotate(180deg);font-size:11px;font-weight:400;color:var(--ink);letter-spacing:.3px}

.section{position:absolute;left:0;width:693px}
.section-inner{position:absolute;left:136px;width:421px}
.section-title{border-top:1px solid var(--rule);padding-top:2px;font-size:9px;font-weight:500;color:var(--ink)}
.copy{font-size:5.6px;line-height:8.6px;font-weight:300;color:var(--text);letter-spacing:.1px}
.copy strong{font-weight:500}

.about{top:376px;height:100px;background:var(--paper-soft)}
.about .section-inner{top:14px}
.about .copy{margin-top:3px}
.about .copy + .copy{margin-top:8px}

.services{top:476px;height:151px;background:var(--slate)}
.services .section-inner{top:8px}
.services .section-title{border-color:#777;color:var(--paper)}
.service-tab{position:absolute;top:509px;width:72px;text-align:center;color:#e6e6e6;font-size:8.5px;font-weight:300}
.service-tab svg{display:block;margin:14px auto 4px}
.service-tab.is-active{background:var(--paper);color:var(--text);height:107px;box-shadow:0 1px 3px rgba(0,0,0,.35)}
.service-tab .tagline{margin-top:8px;font-size:8.5px;font-weight:400;line-height:12px;color:var(--ink)}

.locations{top:627px;height:157px;background:var(--paper-soft)}
.locations .section-inner{top:12px}
.locations .copy{margin-top:3px}
.office-label{position:absolute;font-size:11.5px;font-weight:400;color:var(--ink)}
.office-address{position:absolute;font-size:5.8px;line-height:8px;font-weight:300;color:var(--muted)}

.news{top:784px;height:207px;background:var(--green)}
.news .section-inner{top:9px}
.news .section-title{border-color:#b6d3c0;color:var(--paper)}
.news-thumb{position:absolute;left:137px;width:46px;height:49px;border-radius:4px;background:linear-gradient(160deg,#ffffff,#e3e3e3);box-shadow:0 1px 2px rgba(0,0,0,.3)}
.news-item{position:absolute;left:189px;width:104px;color:var(--paper)}
.news-item h3{font-size:8.5px;font-weight:500;line-height:10px}
.news-item p{font-size:5px;line-height:7px;font-weight:300;margin-top:1px}
.more{position:absolute;left:275px;width:8px;height:8px;border:1px solid var(--paper);border-radius:50%}
.more::before,.more::after{content:"";position:absolute;background:var(--paper);left:1.5px;top:2.5px;width:3px;height:1px}
.more::after{left:2.5px;top:1.5px;width:1px;height:3px}
.feed-panel{position:absolute;left:307px;top:815px;width:250px;height:160px;border-radius:6px;overflow:hidden;background:radial-gradient(ellipse at 50% 45%,#e9d2a9 0%,#c59d66 45%,#8a6a44 100%);box-shadow:0 2px 4px rgba(0,0,0,.3)}
.feed-panel svg{position:absolute;inset:0}

.follow{top:991px;height:25px;background:var(--paper);display:flex;align-items:center;justify-content:center;gap:14px}
.follow h2{font-size:14px;font-weight:400;color:var(--ink)}
.social{display:flex;gap:10px;font-size:9px;font-weight:500;color:var(--slate)}

.site-footer{top:1016px;height:184px;background:var(--footer);color:var(--footer-type)}
.partners-title{position:absolute;left:139px;top:18px;font-size:11px;font-weight:300}
.partner{position:absolute;height:22px;border-radius:4px;background:var(--footer-tile)}
.partner.is-featured{background:var(--gold)}
.carousel-arrow{position:absolute;top:47px;font-size:10px;font-weight:500}
.footer-nav{position:absolute;right:123px;top:26px;text-align:right;list-style:none;font-size:11px;font-weight:300;line-height:15.8px}
.copyright{position:absolute;left:0;width:693px;top:146px;text-align:center;font-size:13px;font-weight:300;color:var(--copyright)}
</style>
</head>
<body>

<header class="site-header">
  <div class="brand"><span class="brand-mark"></span>PLENVARO</div>
  <nav class="main-nav">
    <span class="is-current">HOME</span><span class="sep">◇</span>
    <span>ABOUT US</span><span class="sep">◇</span>
    <span>OUR SERVICES</span><span class="sep">◇</span>
    <span>NEWS</span><span class="sep">◇</span>
    <span>LOCATIONS</span><span class="sep">◇</span>
    <span>BUISNESS UNITS</span>
  </nav>
</header>

<section class="hero">
  <div class="hero-photo" role="img" aria-label="Photo of a person writing in a notebook at a wooden desk, wearing a wristwatch"></div>
  <svg class="hero-graphic" width="693" height="326" viewBox="0 0 693 326">
    <polygon points="347,27 462,84 462,232 347,289 232,232 232,84" fill="#ffffff"/>
    <text x="347" y="118" text-anchor="middle" font-family="Oswald,sans-serif" font-weight="200" font-size="56" fill="#1d1d1d">MEET</text>
    <text x="347" y="171" text-anchor="middle" font-family="Oswald,sans-serif" font-weight="200" font-size="56" fill="#1d1d1d">YOUR</text>
    <text x="347" y="225" text-anchor="middle" font-family="Oswald,sans-serif" font-weight="700" font-size="56" fill="#1d1d1d">GOALS.</text>
    <polygon points="312,240 382,240 388,286 347,312 306,286" fill="#3a3a3a"/>
    <polyline points="312,303 347,324 382,303" fill="none" stroke="#3a3a3a" stroke-width="3"/>
    <text x="347" y="283" text-anchor="middle" font-family="Oswald,sans-serif" font-weight="500" font-size="24" fill="#ffffff">NOW</text>
  </svg>
  <div class="contact-tab"><span>CONTACT US</span></div>
</section>

<section class="section about">
  <div class="section-inner">
    <h2 class="section-title">ABOUT US</h2>
    <p class="copy">We specialize in delivering quality professional services and technical projects that support larger business goals. We understand that most technical projects are conceptualized to support a larger vision with actual business goals in mind and ensure that all of our professional and certified expertise is included in our professional DED in our professional services to meet those goals.</p>
    <p class="copy">Our ultimate goal is to provide quality, technical and professional services on projects of any scale and/or complexity, from conception through to completion. Our philosophy is simple: <strong>stick to what you are good at and be the best at it.</strong></p>
  </div>
</section>

<section class="section services">
  <div class="section-inner">
    <h2 class="section-title">OUR SERVICES</h2>
  </div>
</section>
<div class="service-tab is-active" style="left:167px">
  <svg width="26" height="24" viewBox="0 0 26 24" fill="none" stroke="#333" stroke-width="1.1"><rect x="3" y="4" width="15" height="18"/><line x1="6" y1="10" x2="14" y2="10"/><line x1="6" y1="14" x2="14" y2="14"/><line x1="6" y1="18" x2="11" y2="18"/><line x1="12" y1="15" x2="24" y2="2"/></svg>
  CONSULTING
  <p class="tagline">LET'S<br>DELIBERATE<br>TOGETHER.</p>
</div>
<div class="service-tab" style="left:232px">
  <svg width="24" height="24" viewBox="0 0 24 24" fill="none" stroke="#e6e6e6" stroke-width="1.1"><circle cx="12" cy="9" r="6"/><path d="M9 15v4h6v-4"/><line x1="10" y1="21" x2="14" y2="21"/></svg>
  ENGINEERING
</div>
<div class="service-tab" style="left:303px">
  <svg width="24" height="24" viewBox="0 0 24 24" fill="none" stroke="#e6e6e6" stroke-width="1.1"><ellipse cx="12" cy="6" rx="8" ry="3"/><path d="M4 6v12c0 1.7 3.6 3 8 3s8-1.3 8-3V6"/><path d="M4 12c0 1.7 3.6 3 8 3s8-1.3 8-3"/></svg>
  CONSTRUCTION
</div>
<div class="service-tab" style="left:372px">
  <svg width="24" height="24" viewBox="0 0 24 24" fill="none" stroke="#e6e6e6" stroke-width="1.1"><rect x="3" y="4" width="18" height="12"/><line x1="12" y1="16" x2="12" y2="20"/><line x1="7" y1="21" x2="17" y2="21"/></svg>
  OPERATIONS
</div>
<div class="service-tab" style="left:442px">
  <svg width="26" height="24" viewBox="0 0 26 24" fill="none" stroke="#e6e6e6" stroke-width="1.4"><line x1="4" y1="4" x2="20" y2="20"/><line x1="20" y1="4" x2="6" y2="18"/><circle cx="20" cy="4" r="2.5"/><circle cx="5" cy="19" r="2.5"/></svg>
  MAINTENANCE
</div>

<section class="section locations">
  <div class="section-inner">
    <h2 class="section-title">LOCATIONS</h2>
    <p class="copy">We are a systems architecture, project/construction management and consultancy firm, based in Bangkok, Thailand, with offices opening in the Middle East in the near future specializing in project and construction management, engineering, design services and turn-key solutions for technical systems for projects. Plenvaro focus is on providing quality systems design, construction and integration, using recognized international industry standards and recognized international codes and practices.</p>
  </div>
</section>
<svg style="position:absolute;left:195px;top:711px" width="22" height="30" viewBox="0 0 22 30" fill="none" stroke="#555" stroke-width="1.1"><path d="M11 28C5 19 2 14 2 10a9 9 0 0 1 18 0c0 4-3 9-9 18z"/><circle cx="11" cy="10" r="3.5"/></svg>
<div class="office-label" style="left:185px;top:746px">BANGKOK</div>
<div class="office-address" style="left:234px;top:723px">52 THANON RIMKLONG 7<br>BANG CHAK KHET PHRA KHANONG BANGKOK<br>THAILAND</div>
<svg style="position:absolute;left:358px;top:704px" width="40" height="40" viewBox="0 0 40 40" fill="none" stroke="#555" stroke-width="1.1"><circle cx="20" cy="20" r="17"/><ellipse cx="20" cy="20" rx="7" ry="17"/><line x1="3" y1="20" x2="37" y2="20"/><path d="M6 11h28M6 29h28"/></svg>
<div class="office-label" style="left:351px;top:746px">MIDDLE EAST</div>
<div class="office-address" style="left:428px;top:730px">YOUR ADRESSES GO HERE</div>

<section class="section news">
  <div class="section-inner">
    <h2 class="section-title">NEWS</h2>
  </div>
</section>
<div class="news-thumb" style="top:815px" role="img" aria-label="Sketch illustration of a businessman"></div>
<div class="news-item" style="top:817px"><h3>PLENVARO SPREADS IN CHINA</h3><p>It is a long established fact that a reader will be distracted by the readable content of a page when looking at its layout.</p></div>
<div class="more" style="top:854px"></div>
<div class="news-thumb" style="top:871px" role="img" aria-label="Sketch illustration of a pie chart"></div>
<div class="news-item" style="top:876px"><h3>PLENVARO SPREADS IN CHINA</h3><p>It is a long established fact that a reader will be distracted by the readable content of a page when looking at its layout.</p></div>
<div class="more" style="top:912px"></div>
<div class="news-thumb" style="top:929px" role="img" aria-label="Sketch illustration of a rising bar chart"></div>
<div class="news-item" style="top:931px"><h3>PLENVARO SPREADS IN CHINA</h3><p>It is a long established fact that a reader will be distracted by the readable content of a page when looking at its layout.</p></div>
<div class="more" style="top:969px"></div>
<div class="feed-panel" role="img" aria-label="Blurred warm office background behind the news feed badge">
  <svg width="250" height="160" viewBox="0 0 250 160">
    <polygon points="135,15 187,45 187,105 135,135 83,105 83,45" fill="var(--gold)"/>
    <polygon points="135,75 187,105 135,135" fill="var(--gold-deep)"/>
    <text x="135" y="62" text-anchor="middle" font-family="Oswald,sans-serif" font-weight="300" font-size="24" fill="#ffffff">RSS</text>
    <text x="135" y="88" text-anchor="middle" font-family="Oswald,sans-serif" font-weight="200" font-size="20" fill="#ffffff">OR</text>
    <text x="135" y="116" text-anchor="middle" font-family="Oswald,sans-serif" font-weight="400" font-size="26" fill="#ffffff">BLOG</text>
  </svg>
</div>

<section class="section follow">
  <h2>FOLLOW US ON</h2>
  <div class="social"><span>CIRCLR</span><span>CHATTERLY</span><span>CHIRPNET</span></div>
</section>

<footer class="section site-footer">
  <h2 class="partners-title">OUR PARTNERS</h2>
  <span class="carousel-arrow" style="left:183px">&lt;</span>
  <span class="carousel-arrow" style="left:372px">&gt;</span>
  <div class="partner" style="left:193px;top:45px;width:42px"></div>
  <div class="partner is-featured" style="left:239px;top:42px;width:84px;height:28px"></div>
  <div class="partner" style="left:326px;top:45px;width:42px"></div>
  <div class="partner" style="left:193px;top:72px;width:42px"></div>
  <div class="partner" style="left:240px;top:72px;width:42px"></div>
  <div class="partner" style="left:287px;top:72px;width:41px"></div>
  <div class="partner" style="left:331px;top:72px;width:41px"></div>
  <div class="partner" style="left:196px;top:99px;width:42px"></div>
  <div class="partner" style="left:242px;top:99px;width:42px"></div>
  <div class="partner" style="left:288px;top:99px;width:41px"></div>
  <div class="partner" style="left:333px;top:99px;width:41px"></div>
  <ul class="footer-nav">
    <li>ABOUT US</li><li>OUR SERVICES</li><li>NEWS</li><li>LOCATIONS</li><li>BUISNESS UNITS</li><li>TERMS</li><li>PRIVACY</li>
  </ul>
  <p class="copyright">ALL COPYRIGHT IS RESERVED. PLENVARO TECHNOLOGY INC.</p>
</footer>

</body>
</html>
```